Business Card Design - Law Firm

I need a business card design. I have attached a picture of the law firm's website and logo. The business card design should be consistent with those pictures. There should be a place for the employee name, employee job title, telephone number, facsimile number, address, website url, and email address for each employee.
Industry/Entity Type
Business

```html
<!DOCTYPE html>
<html lang="en">
<head>
<meta charset="utf-8">
<title>Marrowick Law — Business Card</title>
<link rel="stylesheet" href="https://fonts.googleapis.com/css2?family=Arimo:wght@400;700&family=Libre+Baskerville:wght@400&display=swap">
<style>
  :root {
    --backdrop: #e6e3de;
    --card: #ffffff;
    --gold: #a8913a;
    --ink: #111111;
    --band: #141414;
    --rule: #c9c9c9;
  }
  * { margin: 0; padding: 0; box-sizing: border-box; }
  html, body {
    width: 1200px; height: 821px; overflow: hidden;
    background: var(--backdrop);
    font-family: "Arimo", Arial, sans-serif;
  }
  .sheet {
    position: relative; width: 1200px; height: 821px;
    display: flex; align-items: center; justify-content: center; gap: 40px;
  }
  .card {
    position: relative; width: 540px; height: 309px;
    background: var(--card); border-radius: 14px; overflow: hidden;
    box-shadow: 0 6px 18px rgba(0,0,0,0.18);
  }
  .card__band {
    position: absolute; left: 0; right: 0; bottom: 0; height: 44px;
    background: var(--band);
    border-top: 5px solid var(--gold);
    display: flex; align-items: center; justify-content: center;
  }
  .card--front .card__band { height: 34px; }
  .band__url { color: #fff; font-size: 16px; font-weight: 700; letter-spacing: 0.3px; }

  /* Wordmark */
  .brand { position: absolute; display: flex; align-items: center; gap: 14px; }
  .brand__mark { width: 50px; height: 50px; background: var(--ink); flex: none; }
  .brand__sep { width: 1px; height: 58px; background: var(--rule); flex: none; }
  .brand__text {
    display: flex; flex-direction: column; align-items: center;
    font-family: "Libre Baskerville", "Times New Roman", serif;
    font-weight: 400; color: var(--gold);
  }
  .brand__name { font-size: 36px; line-height: 1; letter-spacing: 0.5px; white-space: nowrap; }
  .brand__sub {
    display: flex; align-items: center; gap: 10px; width: 100%;
    font-size: 11px; letter-spacing: 2px; margin-top: 6px;
  }
  .brand__sub::before, .brand__sub::after {
    content: ""; flex: 1; height: 1px; background: var(--rule);
  }
  .card--front .brand { left: 50%; top: 26px; transform: translateX(-50%); }
  .card--back .brand { left: 50%; top: 96px; transform: translateX(-50%); }

  /* Person */
  .person { position: absolute; right: 296px; top: 176px; text-align: right; }
  .person__name { color: var(--gold); font-size: 22px; font-weight: 700; line-height: 1.1; white-space: nowrap; }
  .person__title { color: var(--ink); font-size: 13px; margin-top: 2px; }

  .divider { position: absolute; left: 262px; top: 128px; width: 1px; height: 124px; background: var(--ink); }

  /* Contact */
  .contact { position: absolute; left: 280px; top: 128px; color: var(--ink); }
  .contact__address { font-size: 14px; line-height: 1.35; margin-bottom: 6px; }
  .contact__list { list-style: none; }
  .contact__item { display: flex; align-items: center; gap: 8px; font-size: 14px; line-height: 20px; }
  .contact__label { color: var(--gold); font-weight: 700; width: 14px; }
  .contact__icon { width: 14px; height: 14px; flex: none; }
</style>
</head>
<body>
<main class="sheet">

  <section class="card card--front" aria-label="Card front">
    <div class="brand">
      <span class="brand__mark"></span>
      <span class="brand__sep"></span>
      <span class="brand__text">
        <span class="brand__name">Marrowick</span>
        <span class="brand__sub">LAW</span>
      </span>
    </div>

    <div class="person">
      <p class="person__name">Daniel Harper</p>
      <p class="person__title">President</p>
    </div>

    <span class="divider"></span>

    <div class="contact">
      <p class="contact__address">48 Linden Court, Suite 310<br>Ashford, Vermont 0518</p>
      <ul class="contact__list">
        <li class="contact__item">
          <svg class="contact__icon" viewBox="0 0 16 16" aria-hidden="true">
            <path d="M2 5 Q2 2 8 2 Q14 2 14 5 L11 6 L10 4.5 Q8 4 6 4.5 L5 6 Z" fill="var(--gold)"/>
            <path d="M4 7 H12 L14 14 H2 Z" fill="var(--gold)"/>
            <circle cx="8" cy="10.5" r="2" fill="#fff"/>
          </svg>
          555.204.6318
        </li>
        <li class="contact__item">
          <svg class="contact__icon" viewBox="0 0 16 16" aria-hidden="true">
            <rect x="4" y="1" width="8" height="5" fill="var(--gold)"/>
            <rect x="1" y="6" width="14" height="7" rx="1" fill="var(--gold)"/>
            <rect x="4" y="10" width="8" height="5" fill="#fff" stroke="var(--gold)" stroke-width="1"/>
          </svg>
          555.204.6319
        </li>
        <li class="contact__item">
          <svg class="contact__icon" viewBox="0 0 16 16" aria-hidden="true">
            <rect x="1" y="3" width="14" height="10" fill="var(--gold)"/>
            <path d="M1 3 L8 9 L15 3" fill="none" stroke="#fff" stroke-width="1.2"/>
          </svg>
          daniel@marrowicklaw.com
        </li>
        <li class="contact__item">
          <svg class="contact__icon" viewBox="0 0 16 16" aria-hidden="true">
            <circle cx="8" cy="8" r="7" fill="var(--gold)"/>
            <g fill="none" stroke="#fff" stroke-width="0.9">
              <ellipse cx="8" cy="8" rx="3" ry="7"/>
              <line x1="1" y1="8" x2="15" y2="8"/>
              <line x1="8" y1="1" x2="8" y2="15"/>
            </g>
          </svg>
          www.marrowicklaw.com
        </li>
      </ul>
    </div>

    <div class="card__band"></div>
  </section>

  <section class="card card--back" aria-label="Card back">
    <div class="brand">
      <span class="brand__mark"></span>
      <span class="brand__sep"></span>
      <span class="brand__text">
        <span class="brand__name">Marrowick</span>
        <span class="brand__sub">LAW</span>
      </span>
    </div>
    <div class="card__band">
      <span class="band__url">www.marrowicklaw.com</span>
    </div>
  </section>

</main>
</body>
</html>
```